Kestrel Computer Repairs Web Banner

We're after a catchy web banner to advertise the computer repairs business on other web sites and affiliate sites. We manage software, hardware repairs, component upgrades, virus and malware removal and provide online backup solutions.
Please incorporate the logo designed by Quokka, and add our phone number, 1300 482 956 to the banner. The banner will link to the website homepage.

```html
<!DOCTYPE html>
<html lang="en">
<head>
<meta charset="utf-8">
<title>Kestrel Computer Repairs Web Banner</title>
<link href="https://fonts.googleapis.com/css2?family=Roboto+Condensed:wght@700&display=swap" rel="stylesheet">
<style>
  :root {
    --page: #ffffff;
    --sky-light: #6cc0ee;
    --sky-deep: #1a7cc6;
    --pixel-red: #e1141b;
    --pixel-white: rgba(255, 255, 255, 0.9);
    --call-blue: #1f7fc4;
    --brand-blue: #1b5fa8;
    --text-light: #ffffff;
  }
  html, body {
    margin: 0;
    width: 1200px;
    height: 718px;
    overflow: hidden;
    background: var(--page);
  }
  .canvas {
    position: relative;
    width: 1200px;
    height: 718px;
    font-family: "Roboto Condensed", "Arial Narrow", sans-serif;
  }
  .banner-art {
    position: absolute;
    left: 0;
    top: 0;
  }
  .services {
    position: absolute;
    left: 291px;
    top: 98px;
    margin: 0;
    padding: 0;
    list-style: none;
    color: var(--text-light);
    font-size: 26px;
    line-height: 35px;
    letter-spacing: 0.2px;
  }
  .brand {
    position: absolute;
    left: 284px;
    top: 476px;
    width: 200px;
    display: flex;
    flex-direction: column;
    align-items: flex-start;
    gap: 12px;
    color: var(--brand-blue);
    font-size: 30px;
    line-height: 32px;
  }
  .brand-dot {
    width: 44px;
    height: 44px;
    border-radius: 50%;
    background: var(--brand-blue);
  }
  .click-to {
    position: absolute;
    right: 285px;
    top: 488px;
    margin: 0;
    color: var(--pixel-red);
    font-size: 48px;
    line-height: 56px;
  }
  .call-button {
    position: absolute;
    left: 528px;
    top: 549px;
    width: 403px;
    height: 83px;
    border-radius: 12px 0 0 12px;
    background: var(--call-blue);
    color: var(--text-light);
    font-size: 46px;
    line-height: 83px;
    text-align: center;
    text-decoration: none;
  }
</style>
</head>
<body>
<div class="canvas">
  <svg class="banner-art" width="1200" height="718" viewBox="0 0 1200 718">
    <defs>
      <linearGradient id="sky" x1="0" y1="0" x2="1" y2="0.4">
        <stop offset="0" stop-color="var(--sky-light)"/>
        <stop offset="1" stop-color="var(--sky-deep)"/>
      </linearGradient>
    </defs>
    <rect class="sky-panel" x="272" y="80" width="659" height="365" fill="url(#sky)"/>
    <path class="pixel-block-top" role="img" aria-label="Red pixel square cluster"
          fill="var(--pixel-red)"
          d="M672 80 H931 V144 H864 V100 H752 V144 H672 Z"/>
    <path class="pixel-block-left" role="img" aria-label="Red pixel square steps"
          fill="var(--pixel-red)"
          d="M272 312 H328 V339 H445 V368 H499 V419 H272 Z"/>
    <path class="pixel-block-white" role="img" aria-label="White pixel square steps"
          fill="var(--pixel-white)"
          d="M536 320 H600 V300 H770 V285 H931 V445 H536 Z"/>
  </svg>

  <ul class="services">
    <li>Manage Software</li>
    <li>Hardware Repairs</li>
    <li>Component Upgrades,</li>
    <li>Virus &amp; Malware Removal</li>
    <li>Online Backup Solutions.</li>
  </ul>

  <div class="brand">
    <span class="brand-dot"></span>
    <span class="brand-name">Kestrel Computer Repairs</span>
  </div>

  <p class="click-to">CLICK TO</p>
  <a class="call-button" href="tel:1300482956">Call 1300 482 956</a>
</div>
</body>
</html>
```